Packaging Design for Box Containing Beautiful Copper Mugs

I need a design for a set of two 16 oz copper mugs normally used for Moscow Mules (picture attached). The box dimensions are 19 x 11 x 11 cm and it opens from the top. An example of some of the boxes the manufacturer has made in the past is attached (note: some are single, not double like I need). I would either like a "retro" like feel to the box, as it is a classic type mug from the 1950s/1960s or an "eco-feel" with matte cardboard and green/dark brown or black lettering - or get creative and see if you have a better idea! I have a logo I will need on it as well as a barcode on the bottom and the product description. It also needs to say made in India and lifetime guarantee somewhere on the box. I do have some text to add somewhere on two of the sides but the design needs to be right before I add it. So you can use a placeholder for the text and I can add it when we decide on the design. I would like it to be the kind of box you would give to a friend as a gift; As beautiful on the outside as on the inside.

Feel free to ask any questions. Thanks!

Target Market(s)

21-65 year olds who like Moscow Mules

Industry/Entity Type

Home And Garden

Font styles to use
Sans Serif

Requirements
Must have
• A design that stands apart and makes you want to grab one off the shelf and give one to a friend as a nice gift.
Nice to have
• Stylish, unique, grabs your attention

```html
<!DOCTYPE html>
<html lang="en">
<head>
<meta charset="utf-8">
<title>Copper Mug Gift Box – Dieline</title>
<link rel="stylesheet" href="https://fonts.googleapis.com/css2?family=Great+Vibes&family=Montserrat:wght@600;700&display=swap">
<style>
  :root {
    --backdrop: #969696;
    --teal: #438c91;
    --pattern-cream: #f3f4dc;
    --pattern-mint: #d6e6d8;
    --pattern-teal: #a9cbc6;
    --label-fill: #fbfbe8;
    --script-red: #c0282f;
    --ink: #2b2b2b;
    --white: #ffffff;
    --copper-light: #d58a5a;
    --copper-dark: #7a3a1c;
  }
  html, body {
    margin: 0;
    padding: 0;
    width: 1200px;
    height: 1200px;
    overflow: hidden;
    background: var(--backdrop);
  }
  .canvas {
    position: relative;
    width: 1200px;
    height: 1200px;
  }
  .dieline {
    position: absolute;
    left: 50px;
    top: 275px;
    width: 1100px;
    height: 649px;
  }
  .panel-teal { fill: var(--teal); }
  .label-outer {
    fill: var(--label-fill);
    stroke: var(--teal);
    stroke-width: 0.5;
  }
  .label-inner {
    fill: none;
    stroke: var(--teal);
    stroke-width: 0.9;
    stroke-dasharray: 2 1.4;
  }
  .label-rule { stroke: var(--teal); stroke-width: 0.8; }
  .brand-name {
    font-family: "Great Vibes", cursive;
    fill: var(--script-red);
  }
  .product-name {
    font-family: "Great Vibes", cursive;
    fill: var(--script-red);
  }
  .guarantee {
    font-family: "Montserrat", sans-serif;
    font-weight: 600;
    fill: var(--ink);
  }
  .origin {
    font-family: "Montserrat", sans-serif;
    font-weight: 700;
    fill: var(--white);
    letter-spacing: 0.2px;
  }
</style>
</head>
<body>
<main class="canvas">
  <svg class="dieline" viewBox="105 490 805 475" xmlns="http://www.w3.org/2000/svg">
    <defs>
      <radialGradient id="floral-tone" cx="0.5" cy="0.45" r="0.8">
        <stop offset="0" stop-color="var(--pattern-cream)"/>
        <stop offset="0.6" stop-color="var(--pattern-mint)"/>
        <stop offset="1" stop-color="var(--pattern-teal)"/>
      </radialGradient>
      <linearGradient id="copper-tone" x1="0" y1="0" x2="1" y2="0">
        <stop offset="0" stop-color="var(--copper-dark)"/>
        <stop offset="0.5" stop-color="var(--copper-light)"/>
        <stop offset="1" stop-color="var(--copper-dark)"/>
      </linearGradient>
      <path id="label-shape" d="M9,4 H36 Q51,-2 66,4 H93 A9 9 0 0 0 102,13 V73 A9 9 0 0 0 93,82 H66 Q51,88 36,82 H9 A9 9 0 0 0 0,73 V13 A9 9 0 0 0 9,4 Z"/>
      <g id="product-label">
        <use href="#label-shape" class="label-outer"/>
        <use href="#label-shape" class="label-inner" transform="translate(4.1 3.5) scale(0.92)"/>
        <text class="brand-name" x="51" y="34" font-size="24" text-anchor="middle">Logo</text>
        <line class="label-rule" x1="36" y1="44" x2="66" y2="44"/>
        <text class="product-name" x="51" y="63" font-size="13.5" text-anchor="middle">Coffee Mug</text>
        <text class="guarantee" x="51" y="74" font-size="5.2" text-anchor="middle">Lifetime Guarantee</text>
      </g>
    </defs>

    <!-- left dust flap -->
    <polygon class="panel-teal flap-left" points="150,588 260,588 260,868 150,868 112,830 112,628"/>

    <!-- front panel -->
    <g class="panel-front">
      <path class="panel-teal" d="M260,868 V505 Q260,497 268,497 H494 Q502,497 502,505 V868 Z"/>
      <rect x="260" y="515" width="242" height="353" fill="url(#floral-tone)" role="img" aria-label="Teal floral swirl pattern on cream"/>
      <use href="#product-label" transform="translate(334 684)"/>
    </g>

    <!-- side panel -->
    <g class="panel-side">
      <polygon class="panel-teal" points="502,588 605,588 640,625 640,832 605,868 502,868"/>
      <rect x="513" y="680" width="98" height="82" rx="6" fill="url(#copper-tone)" role="img" aria-label="Photo of a hammered copper mug with mint and a lime slice"/>
      <text class="origin" x="515" y="789" font-size="5.5">MADE IN INDIA</text>
    </g>

    <!-- back panel -->
    <g class="panel-back">
      <path class="panel-teal" d="M640,648 Q640,640 648,640 H877 Q885,640 885,648 V958 H640 Z"/>
      <rect x="640" y="640" width="245" height="300" fill="url(#floral-tone)" role="img" aria-label="Teal floral swirl pattern on cream"/>
      <use href="#product-label" transform="translate(713 684)"/>
    </g>

    <!-- glue flap -->
    <polygon class="panel-teal flap-glue" points="885,660 905,668 905,932 885,940"/>
  </svg>
</main>
</body>
</html>
```